Creative Business Card for my Sail Boat.. Tide & Drift

Going to order PLASTIC business cards for my boat.. she is a sailing vessel catamaran named Tide & Drift..

Target Market(s)

to impress other boaters with a unique designed plastic card

Contact Information for Business Card

S/V Tide & Drift
Captain Carl Denby
denby@carl.example
Mobile/WhatsApp 1-555-318-7620
www.sailtideanddrift.example

Requirements
Must have
• Cool colors. logo.. and info in Business Card Details.. Thanks! Utilize clear or cloudy plastic in design. Thanks

```html
<!DOCTYPE html>
<html lang="en">
<head>
<meta charset="utf-8">
<title>Tide &amp; Drift — Business Card</title>
<link rel="stylesheet" href="https://fonts.googleapis.com/css2?family=Montserrat:wght@400;500&family=Roboto:wght@700;900&display=swap">
<style>
  :root {
    --page-bg: #e9e3dc;
    --card-tint: rgba(78, 36, 20, 0.82);
    --card-tint-deep: rgba(60, 26, 14, 0.88);
    --frost-sheen: rgba(255, 255, 255, 0.10);
    --card-edge: rgba(255, 255, 255, 0.38);
    --logo-ink: rgba(222, 214, 208, 0.82);
    --name-ink: #a8958a;
    --contact-ink: #ae9e94;
    --accent-green: #2c8a3a;
    --accent-red: #b0232a;
    --glow-green: rgba(44, 138, 58, 0.55);
    --glow-red: rgba(176, 35, 42, 0.55);
  }
  * { margin: 0; padding: 0; box-sizing: border-box; }
  html, body {
    width: 1200px;
    height: 1200px;
    overflow: hidden;
    background: var(--page-bg);
  }
  .canvas {
    position: relative;
    width: 1200px;
    height: 1200px;
  }
  .card {
    position: absolute;
    left: 100px;
    top: 328px;
    width: 1000px;
    height: 543px;
    border-radius: 30px;
    background:
      linear-gradient(115deg, var(--frost-sheen) 0%, rgba(255,255,255,0) 40%, rgba(255,255,255,0.06) 70%, rgba(255,255,255,0) 100%),
      linear-gradient(165deg, var(--card-tint) 0%, var(--card-tint-deep) 100%);
    box-shadow:
      inset 0 0 0 2px var(--card-edge),
      inset 0 0 24px rgba(255, 255, 255, 0.12),
      0 14px 34px rgba(70, 40, 25, 0.16);
    overflow: hidden;
  }
  .decor-field {
    position: absolute;
    inset: 0;
    background:
      radial-gradient(ellipse 260px 230px at 84% 18%, var(--glow-green) 0%, rgba(44, 138, 58, 0.22) 55%, rgba(44, 138, 58, 0) 100%),
      radial-gradient(ellipse 240px 210px at 87% 80%, var(--glow-red) 0%, rgba(176, 35, 42, 0.2) 55%, rgba(176, 35, 42, 0) 100%);
  }
  .brand {
    position: absolute;
    left: 56px;
    top: 34px;
    display: flex;
    align-items: flex-start;
    gap: 14px;
  }
  .brand-name {
    font-family: "Roboto", sans-serif;
    font-weight: 900;
    font-size: 92px;
    line-height: 1.0;
    color: var(--logo-ink);
    letter-spacing: -1px;
  }
  .brand-mark {
    margin-top: 24px;
    width: 82px;
    height: 82px;
    border: 7px solid var(--accent-green);
    border-radius: 50%;
    flex: none;
  }
  .captain {
    position: absolute;
    left: 50px;
    top: 300px;
    font-family: "Roboto", sans-serif;
    font-weight: 700;
    font-size: 30px;
    letter-spacing: 0.2px;
    color: var(--name-ink);
  }
  .contact {
    position: absolute;
    left: 50px;
    top: 390px;
    list-style: none;
    font-family: "Montserrat", sans-serif;
    font-weight: 400;
    font-size: 25px;
    line-height: 38px;
    color: var(--contact-ink);
  }
  .contact-phone {
    display: flex;
    align-items: center;
    gap: 12px;
  }
  .contact-icon { display: block; }
</style>
</head>
<body>
<div class="canvas">
  <div class="card">
    <div class="decor-field" role="img" aria-label="Large brand emblem decoration in green and red on the right side"></div>

    <div class="brand">
      <span class="brand-name">Tide &amp;<br>Drift</span>
      <span class="brand-mark"></span>
    </div>

    <p class="captain">CAPTAIN CARL DENBY</p>

    <ul class="contact">
      <li class="contact-phone">
        <span>1-555-318-7620</span>
        <svg class="contact-icon" width="16" height="24" viewBox="0 0 16 24" aria-label="mobile">
          <rect x="1.5" y="1.5" width="13" height="21" rx="2.5" fill="none" stroke="var(--accent-green)" stroke-width="2.5"/>
          <line x1="6" y1="18.5" x2="10" y2="18.5" stroke="var(--accent-green)" stroke-width="2"/>
        </svg>
        <svg class="contact-icon" width="24" height="24" viewBox="0 0 24 24" aria-label="chat">
          <circle cx="12" cy="12" r="9.5" fill="none" stroke="var(--accent-green)" stroke-width="2.5"/>
        </svg>
      </li>
      <li>denby@carl.example</li>
      <li>www.sailtideanddrift.example</li>
    </ul>
  </div>
</div>
</body>
</html>
```